Stylish Business Card for Modern hair salon

I need a simple business card design using our salon logo and colours that are in the logo. We service clients of all ages but predominantly those in the 18 to 55 age range. We have a young staff and are looking to have a card that will present a modern and clean image that represents who we are. The card should be in black and white same as our logo. Minimal use of other colours is allowed.

Industry/Entity Type

Hair And Beauty

Contact Information for Business Card

The design should have the following information
salon name - TZ Hair Studio
address - 2957 Fernbrook Rd.W. Mississauga, ON L8R3P2
phone - 905 641-2087
website - tzhairexample.ca
instagram - tz.hairstudio
twitter - @TZ_HairStudio

Colors
000000
ffffff
474747

Requirements
Must have
• simple design, salon name, address, phone, website, instagram, twitter info
• Back of card should have the following:
• YOUR NEXT APPOINTMENT
• DATE
• TIME
Nice to have
• simple design, clear to see and read,
• predominantly black and white colour, minimal use of other colours is ok
Should not have
• many colours, various fonts

```html
<!DOCTYPE html>
<html lang="en">
<head>
<meta charset="utf-8">
<title>TZ Hair Studio – Business Card</title>
<link rel="stylesheet" href="https://fonts.googleapis.com/css2?family=Tinos:wght@400;700&display=swap">
<style>
  :root {
    --ink: #000000;
    --paper: #ffffff;
    --slate: #474747;
    --mist: #9a9a9a;
    --backdrop: #e9e9e9;
  }
  * { margin: 0; padding: 0; box-sizing: border-box; }
  html, body {
    width: 1200px; height: 892px; overflow: hidden;
    background: var(--backdrop);
    font-family: "Tinos", "Times New Roman", serif;
  }
  .canvas { position: relative; width: 1200px; height: 892px; }

  .card {
    position: absolute; top: 298px;
    width: 525px; height: 300px;
    box-shadow: 0 6px 18px rgba(0,0,0,.18);
    overflow: hidden;
  }

  /* ---------- Front ---------- */
  .card--front { left: 50px; background: var(--paper); color: var(--ink); }
  .card--front .edge-top {
    position: absolute; top: 14px; left: 300px; right: 0; height: 2px; background: var(--mist);
  }
  .card--front .edge-bottom {
    position: absolute; bottom: 14px; left: 0; right: 0; height: 2px; background: var(--mist);
  }
  .card--front .wordmark {
    position: absolute; top: 40px; left: 34px;
    font-weight: 700; font-size: 34px; letter-spacing: 2px; line-height: 1;
  }
  .card--front .wordmark-rule {
    position: absolute; top: 86px; left: 34px; width: 230px; height: 1px; background: var(--ink);
  }
  .name-band {
    position: absolute; top: 128px; left: 248px; right: 0; height: 30px;
    background: var(--slate); color: var(--paper);
    font-size: 20px; letter-spacing: 1px; line-height: 30px; padding-left: 40px;
    text-transform: uppercase;
  }
  .name-band svg { position: absolute; left: 0; top: 0; }
  .contact-list {
    position: absolute; top: 172px; right: 26px;
    list-style: none; text-align: right; font-size: 14px; line-height: 21px;
  }
  .contact-list li { display: flex; justify-content: flex-end; align-items: center; gap: 7px; }
  .contact-list .mark {
    width: 13px; height: 13px; border: 1px solid var(--slate); flex: none;
    display: flex; align-items: center; justify-content: center;
  }

  /* ---------- Back ---------- */
  .card--back { right: 50px; background: var(--ink); color: var(--paper); }
  .card--back .edge-top {
    position: absolute; top: 14px; left: 0; width: 250px; height: 2px; background: var(--paper);
  }
  .card--back .edge-bottom {
    position: absolute; bottom: 14px; right: 0; width: 300px; height: 2px; background: var(--paper);
  }
  .card--back .wordmark {
    position: absolute; top: 44px; left: 0; right: 0; text-align: center;
    font-weight: 700; font-size: 34px; letter-spacing: 2px; line-height: 1;
  }
  .card--back .wordmark-rule {
    position: absolute; top: 90px; left: 160px; width: 205px; height: 1px; background: var(--paper);
  }
  .appointment-title {
    position: absolute; top: 118px; left: 0; right: 0; text-align: center;
    font-size: 19px; letter-spacing: 1px;
  }
  .appointment-rule { position: absolute; top: 146px; left: 100px; }
  .appointment-fields {
    position: absolute; top: 180px; left: 40px; right: 40px;
    display: flex; justify-content: space-between; font-size: 15px; letter-spacing: 1px;
  }
  .appointment-fields .field { display: flex; align-items: flex-end; gap: 4px; }
  .appointment-fields .fill {
    display: inline-block; width: 140px; border-bottom: 2px dotted var(--paper); margin-bottom: 4px;
  }
</style>
</head>
<body>
<main class="canvas">

  <section class="card card--front" aria-label="Business card front">
    <div class="edge-top"></div>
    <div class="wordmark">TZ HAIR STUDIO</div>
    <div class="wordmark-rule"></div>

    <div class="name-band">
      <svg width="34" height="30" viewBox="0 0 34 30" aria-hidden="true">
        <polygon points="0,0 10,0 4,30 -6,30" fill="#ffffff"/>
        <polygon points="10,0 18,0 12,30 4,30" fill="#000000"/>
        <polygon points="21,0 26,0 20,30 15,30" fill="#000000"/>
      </svg>
      TZ Hair Studio
    </div>

    <ul class="contact-list">
      <li>2957 Fernbrook Rd.W. Mississauga, ON L8R3P2
        <span class="mark"><svg width="9" height="11" viewBox="0 0 9 11"><path d="M4.5 10.5C1.5 6.5 0.8 5 0.8 3.8a3.7 3.7 0 0 1 7.4 0C8.2 5 7.5 6.5 4.5 10.5z" fill="none" stroke="#474747"/><circle cx="4.5" cy="3.8" r="1.2" fill="#474747"/></svg></span></li>
      <li>905 641-2087
        <span class="mark"><svg width="9" height="9" viewBox="0 0 9 9"><path d="M1.5 1h2l.6 2-1.2.8a5 5 0 0 0 2.3 2.3l.8-1.2 2 .6v2c-4 .4-7-2.6-6.5-6.5z" fill="#474747"/></svg></span></li>
      <li>tzhairexample.ca
        <span class="mark"><svg width="9" height="9" viewBox="0 0 9 9"><circle cx="4.5" cy="4.5" r="3.6" fill="none" stroke="#474747"/><path d="M0.9 4.5h7.2M4.5 0.9c-2 2-2 5.2 0 7.2M4.5 0.9c2 2 2 5.2 0 7.2" fill="none" stroke="#474747" stroke-width=".7"/></svg></span></li>
      <li>tz.hairstudio <span class="mark"></span></li>
      <li>@TZ_HairStudio <span class="mark"></span></li>
    </ul>
    <div class="edge-bottom"></div>
  </section>

  <section class="card card--back" aria-label="Business card back">
    <div class="edge-top"></div>
    <div class="wordmark">TZ HAIR STUDIO</div>
    <div class="wordmark-rule"></div>
    <h2 class="appointment-title">YOUR NEXT APPOINTMENT</h2>
    <svg class="appointment-rule" width="325" height="8" viewBox="0 0 325 8" aria-hidden="true">
      <line x1="0" y1="4" x2="325" y2="4" stroke="#ffffff" stroke-width="1"/>
      <rect x="159" y="1" width="6" height="6" transform="rotate(45 162 4)" fill="#ffffff"/>
    </svg>
    <div class="appointment-fields">
      <div class="field">DATE : <span class="fill"></span></div>
      <div class="field">TIME : <span class="fill"></span></div>
    </div>
    <div class="edge-bottom"></div>
  </section>

</main>
</body>
</html>
```